author needs a Book Cover design

Needs a book cover design that matches the title in some way.
Book Title is- 9 Lanterns Beneath a Quiet Harbor Tonight.
Subtile- Harvest Lessons Across Ordinary Seasons.
Author Name:-Desmond Okorefe, Jr.

Final Design is subject to Book Publisher's requirement.

Font styles to use
Serif

Requirements
Must have
• Follow these recommended specifications for your cover file:
• Page Size: Your cover should be a single (one-piece) PDF that includes the back cover, spine, and front cover. You can submit your cover on any size page as long as the printable area is measured exactly for your book's trim size, spine width, and allows at least .125” bleed, centered horizontally and vertically.
• Minimum Cover Width: Bleed + Back Cover Trim Size + Spine Width + Front Cover Trim Size + Bleed
• Minimum Cover Height: Bleed + Book Height Trim Size + Bleed
• Trim Size: Your cover should be the same trim size as you choose in the Title Information when setting up your book. For example, submitting a cover that was previously used for a 6.25” x 9.25” book would not work for a 6” x 9” book.
• Barcodes: For manufacturing and distribution reasons, your book's back cover must include a valid ISBN barcode. If your cover already has an ISBN barcode, make sure it is high-resolution, or at least 300 dpi, and 1.5" - 2" in width with proportional height. Ideally, this barcode should be 2” wide by 1.2” tall. Also, check to make sure you have the rights to use the ISBN on your cover, because not all services allow you to use their ISBNs elsewhere.
• QR codes: There are no set size restrictions, but the quality (resolution) of the image must be set to at least 300 dpi. Make sure you have the rights to use the code.
• If your artwork does not include a barcode, we will automatically add one in the lower right-hand corner of your book's back cover, free of charge. Our system will place the ISBN barcode in a space 2" wide and 1.2" tall. The bottom of this barcode is located 1/4" up from the bottom trim line of the cover. The right side of the barcode is located 1/4" to the left of the spine. Please ensure that you don't have any important images or text in the barcode location. You can also refer to our Artwork Templates for the exact size and position of the ISBN barcode on your final cover.
• If you don’t have an ISBN already on your cover, but you have live graphic or text elements in the location that our system will place the ISBN, you will need to move those elements or place the ISBN in a different location yourself.
• Publishing Logos: We do not add our logo to your book.
• Spine Width and Variance: If your artwork was created for a different service, please make sure that the spine width of your current cover matches our spine width. Different services may use different paper thickness, which is why the spine width of your cover artwork could be correct for another service but incorrect for our service.
• Ideally, you should avoid hard vertical lines separating your front or back cover panels from your spine and should allow for at least a .125" variance of your spine on each side (for example, the text on a 1" spine should be no larger than .75" wide). For books with a page count of less than 130 pages, we strongly recommend a blank spine.
• Your spine width should be calculated based on the number of pages in your book and using the appropriate formula:
• Black and White Interior Book Spine Width:
• White paper: Number of pages x .002252 = Spine width in inches
• Cream paper: Number of pages x .0025 = Spine width in inches
• Color Interior Book Spine Width:
• Number of pages x .002347 = Spine width in inches
• Example of spine width calculation for a 120-page black and white interior book with white paper:
• 120 x .002252 = .27" spine width
• Text and Image Placement: All live cover elements, or text and images that cannot be cut, must be at least .125" inside the trim lines to ensure no important elements are cut during the bookmaking process and the appearance of your printed books is consistent.
• Bleed: Your cover's background must extend at least .125" beyond the final trim line to accommodate for cutting/trimming tolerance.
• Crop/Registration Marks: Please do not include any crop or registration marks on your files, as they may interfere with the binding process or appear on the cover. We use our own measurements, specific to our systems, for cutting and binding; crop or registration marks placed by you could interfere with this process.
• Images and Fonts: Any images you include on your book's cover may be tagged with your choice of CMYK or RGB profiles or left untagged in a generic color space. All images should be sized at 100%, flattened to one layer and placed in your native document at a resolution of at least 300 DPI. You should also embed all fonts in your PDF file.
• Desmond, I hope this information is helpful to you. Please feel free to contact us if you have any other questions or concerns.
• Best regards,
• *WILL SUPPLY THE PAGE NUMBERS INFORMATION
• Lisbeth
• PrintHollow Member Services
Nice to have
• An attractive design that matches the title. Design can include backgrounds

```html
<!DOCTYPE html>
<html lang="en">
<head>
<meta charset="utf-8">
<title>9 Lanterns Beneath a Quiet Harbor Tonight — Book Cover</title>
<link rel="stylesheet" href="https://fonts.googleapis.com/css2?family=Cinzel:wght@400;500&family=Cinzel+Decorative:wght@400&display=swap">
<style>
  :root {
    --page-bg: #e6e6e6;
    --cover-top: #a9c8e6;
    --cover-bottom: #8fb6e0;
    --title-red: #e1242a;
    --ink: #1f2430;
    --art-light: #7ea9d8;
    --art-dark: #5f92cf;
  }
  * { box-sizing: border-box; margin: 0; padding: 0; }
  html, body {
    width: 1200px;
    height: 1099px;
    overflow: hidden;
    background: var(--page-bg);
  }
  .cover {
    position: absolute;
    left: 280px;
    top: 70px;
    width: 640px;
    height: 960px;
    background: linear-gradient(180deg, var(--cover-top) 0%, var(--cover-top) 45%, var(--cover-bottom) 100%);
    overflow: hidden;
  }
  .author {
    position: absolute;
    top: 42px;
    left: 0;
    width: 100%;
    text-align: center;
    font-family: "Cinzel", serif;
    font-size: 27px;
    letter-spacing: 0.5px;
    color: var(--ink);
  }
  .title {
    position: absolute;
    top: 100px;
    left: 40px;
    right: 40px;
    font-family: "Cinzel Decorative", serif;
    color: var(--title-red);
    font-weight: 400;
  }
  .title-lead {
    display: flex;
    align-items: flex-start;
  }
  .title-numeral {
    font-size: 228px;
    line-height: 0.9;
    margin-right: 6px;
  }
  .title-lead-words {
    display: flex;
    flex-direction: column;
    padding-top: 28px;
  }
  .title-line-xl { font-size: 82px; line-height: 1; }
  .title-line-lg { font-size: 66px; line-height: 1.15; }
  .title-tail {
    text-align: right;
    margin-top: 6px;
  }
  .title-tail span {
    display: block;
    font-size: 58px;
    line-height: 1.1;
  }
  .subtitle {
    position: absolute;
    top: 578px;
    left: 0;
    width: 100%;
    text-align: center;
    font-family: "Cinzel", serif;
    font-size: 23px;
    color: var(--ink);
    letter-spacing: 0.3px;
  }
  .cover-art {
    position: absolute;
    left: 0;
    bottom: 0;
    width: 100%;
    height: 320px;
    background: linear-gradient(180deg, var(--art-light) 0%, var(--art-dark) 100%);
    border-radius: 46% 54% 0 0 / 30% 36% 0 0;
    opacity: 0.75;
  }
</style>
</head>
<body>
  <main class="cover">
    <p class="author">Desmond Okorefe, Jr.</p>
    <h1 class="title">
      <span class="title-lead">
        <span class="title-numeral">9</span>
        <span class="title-lead-words">
          <span class="title-line-xl">Lanterns</span>
          <span class="title-line-lg">Beneath a</span>
        </span>
      </span>
      <span class="title-tail">
        <span>Quiet Harbor</span>
        <span>Tonight</span>
      </span>
    </h1>
    <p class="subtitle">Harvest Lessons Across Ordinary Seasons</p>
    <div class="cover-art" role="img" aria-label="Soft blue silhouette illustration rising from the bottom of the cover"></div>
  </main>
</body>
</html>
```